Luminously Grounded Vitality

We want to design a business card that is modern and appealing for an innovative psychedelic telemedicine company that provides at-home ketamine-assisted therapy along with wellness, longevity, and anti-aging medicines. We want to use our deep purple and white plus other colors you can find on our website. We don't have any strict brand guidelines yet so feel free to get creative. We want a very professional, but technology first modern design that will instill trust, peace, calm, but also be attractive to investors in the healthcare and SaaS space.

```html
<!DOCTYPE html>
<html lang="en">
<head>
<meta charset="utf-8">
<title>Luminously Grounded Vitality — Business Card</title>
<link href="https://fonts.googleapis.com/css2?family=Lato:wght@300;400;700;900&display=swap" rel="stylesheet">
<style>
  :root {
    --purple: #7d67ab;
    --purple-deep: #5f4595;
    --magenta: #a2409a;
    --white: #ffffff;
    --ink: #4a4a55;
    --stage: #e9e7ee;
  }
  * { box-sizing: border-box; margin: 0; padding: 0; }
  html, body { width: 1200px; height: 952px; overflow: hidden; }
  body {
    background: var(--stage);
    font-family: "Lato", sans-serif;
    display: flex;
    align-items: center;
    justify-content: center;
    gap: 44px;
  }
  .card {
    position: relative;
    width: 520px;
    height: 297px;
    border-radius: 22px;
    overflow: hidden;
    box-shadow: 0 10px 28px rgba(40, 30, 70, 0.18);
  }

  /* Front side */
  .card-front { background: var(--white); }
  .holder { position: absolute; left: 34px; top: 32px; }
  .holder-name {
    font-weight: 900;
    font-size: 19px;
    letter-spacing: 1px;
    color: var(--purple-deep);
  }
  .holder-name .surname { color: var(--magenta); }
  .holder-role {
    margin-top: 3px;
    font-size: 12px;
    color: var(--ink);
    letter-spacing: 0.4px;
  }
  .holder-rule {
    width: 38px;
    height: 2px;
    margin-top: 8px;
    background: var(--purple);
  }
  .contact-list {
    position: absolute;
    left: 34px;
    top: 128px;
    list-style: none;
  }
  .contact-item {
    display: flex;
    align-items: flex-start;
    gap: 9px;
    font-size: 10.5px;
    line-height: 1.35;
    color: var(--ink);
    margin-bottom: 7px;
  }
  .contact-icon {
    flex: none;
    width: 15px;
    height: 15px;
    border-radius: 3px;
    background: var(--purple);
    display: flex;
    align-items: center;
    justify-content: center;
  }
  .contact-item:nth-child(even) .contact-icon { background: var(--magenta); }
  .contact-icon svg { width: 9px; height: 9px; }

  .brand-band {
    position: absolute;
    right: 0;
    top: 152px;
    width: 240px;
    height: 62px;
    background: var(--purple);
    border-radius: 14px 0 0 14px;
    display: flex;
    align-items: center;
    gap: 10px;
    padding-left: 18px;
  }
  .brand-dot {
    flex: none;
    width: 14px;
    height: 14px;
    border-radius: 50%;
    background: var(--white);
  }
  .brand-name {
    color: var(--white);
    font-weight: 300;
    font-size: 17px;
    line-height: 1.15;
  }

  /* Back side */
  .card-back { background: var(--purple); }
  .tab {
    position: absolute;
    background: var(--white);
    border-radius: 10px;
  }
  .tab-top { left: 70px; top: -12px; width: 130px; height: 40px; }
  .tab-bottom { right: 70px; bottom: -12px; width: 130px; height: 40px; }
  .back-brand {
    position: absolute;
    inset: 0;
    display: flex;
    align-items: center;
    justify-content: center;
    gap: 14px;
  }
  .back-brand .brand-dot { width: 22px; height: 22px; }
  .back-brand .brand-name { font-size: 27px; }
</style>
</head>
<body>

  <section class="card card-back" aria-label="Card back">
    <div class="tab tab-top"></div>
    <div class="tab tab-bottom"></div>
    <div class="back-brand">
      <span class="brand-dot"></span>
      <span class="brand-name">Luminously Grounded<br>Vitality</span>
    </div>
  </section>

  <section class="card card-front" aria-label="Card front">
    <div class="holder">
      <p class="holder-name">DANIEL M. <span class="surname">AVERILL</span></p>
      <p class="holder-role">Managing Director</p>
      <div class="holder-rule"></div>
    </div>

    <ul class="contact-list">
      <li class="contact-item">
        <span class="contact-icon">
          <svg viewBox="0 0 10 10"><path d="M5 0.5a3.3 3.3 0 0 0-3.3 3.3C1.7 6.3 5 9.5 5 9.5s3.3-3.2 3.3-5.7A3.3 3.3 0 0 0 5 0.5z" fill="#fff"/><circle cx="5" cy="3.8" r="1.2" fill="#7d67ab"/></svg>
        </span>
        <span>2750 Linden Park Avenue<br>Portland, OR 97205</span>
      </li>
      <li class="contact-item">
        <span class="contact-icon">
          <svg viewBox="0 0 10 10"><path d="M2.2 0.8l1.6 2-1 1.1a5.5 5.5 0 0 0 3.3 3.3l1.1-1 2 1.6-1 1.4C4.9 9.2 0.8 5.1 0.8 1.8z" fill="#fff"/></svg>
        </span>
        <span>+00 555 018 42</span>
      </li>
      <li class="contact-item">
        <span class="contact-icon">
          <svg viewBox="0 0 10 10"><rect x="0.8" y="2" width="8.4" height="6" fill="none" stroke="#fff" stroke-width="1"/><path d="M0.8 2L5 5.4 9.2 2" fill="none" stroke="#fff" stroke-width="1"/></svg>
        </span>
        <span>hello@groundedvitality.com</span>
      </li>
      <li class="contact-item">
        <span class="contact-icon">
          <svg viewBox="0 0 10 10"><circle cx="5" cy="5" r="4" fill="none" stroke="#fff" stroke-width="1"/><path d="M1 5h8M5 1c-2 2.4-2 5.6 0 8M5 1c2 2.4 2 5.6 0 8" fill="none" stroke="#fff" stroke-width="0.8"/></svg>
        </span>
        <span>www.groundedvitality.com</span>
      </li>
    </ul>

    <div class="brand-band">
      <span class="brand-dot"></span>
      <span class="brand-name">Luminously Grounded<br>Vitality</span>
    </div>
  </section>

</body>
</html>
```